Web hosting and design company website

Hello
i need a website for my hosting company.
Brindle Peak Servers
http://brindlepeak.example
Should be technical, crisp, corporate and friendly.
needs a products page, contact, about us, portfolio
needs to be a wordpress site
Logo will be provided shortly
colours should be green, yello, blue, white, black

Industry/Entity Type

Information Technology

Coding

Coded - Design and coding required

Number of Pages Required

4 page

Font styles to use
Sans Serif

Colors
fbee3d
fbf289
acd036
cadf82
0692cd
33a6d7
0355a3
faa54b

Requirements
Must have
• about us
• contact us
• products
• portfolio

```html
<!DOCTYPE html>
<html lang="en">
<head>
<meta charset="utf-8">
<title>Brindle Peak Servers</title>
<link href="https://fonts.googleapis.com/css2?family=Bitter:wght@400;700&family=Lato:wght@400;700&display=swap" rel="stylesheet">
<style>
:root{
  --navy:#0355a3;
  --blue:#33a6d7;
  --sky:#0692cd;
  --orange:#faa54b;
  --deep-orange:#f07f14;
  --olive:#b9b10e;
  --lime:#acd036;
  --yellow:#fbee3d;
  --ink:#333;
  --muted:#666;
  --light:#f4f4f4;
  --grey:#e5e5e5;
  --dark:#262626;
}
*{margin:0;padding:0;box-sizing:border-box}
html,body{width:1200px;height:2219px;overflow:hidden}
body{position:relative;background:#fff;font-family:'Lato',sans-serif;color:var(--ink)}
.abs{position:absolute}

/* top bar */
.topbar{left:0;top:0;width:1200px;height:41px;background:var(--navy)}
.topbar .phone{left:765px;top:8px;display:flex;align-items:center;gap:8px;color:#fff;font-size:18px}
.topbar .phone i{width:26px;height:26px;border-radius:50%;background:var(--blue);display:flex;align-items:center;justify-content:center}
.social{top:9px;width:24px;height:24px;border-radius:50%}

/* header */
.header{left:0;top:41px;width:1200px;height:95px;background:#fff}
.brand{left:130px;top:34px;display:flex;align-items:center;gap:10px;font-family:'Bitter',serif;font-weight:700;font-size:24px;color:var(--navy)}
.brand i{width:22px;height:22px;background:var(--orange)}
.nav a{position:absolute;top:43px;font-family:'Bitter',serif;font-size:15px;color:#222;text-decoration:none;letter-spacing:.3px}
.nav a.active{color:var(--orange)}
.nav a.active::after{content:"";position:absolute;left:0;right:0;top:37px;height:5px;background:var(--orange)}
.nav .sep{position:absolute;top:46px;width:1px;height:14px;background:#ccc}

/* hero */
.hero{left:0;top:136px;width:1200px;height:471px;background:linear-gradient(180deg,#3fb2e4 0%,#8fd3ef 55%,#d9f1fb 100%);overflow:hidden}
.hero h1{position:absolute;left:158px;top:140px;font-family:'Bitter',serif;font-weight:700;font-size:54px;color:#f2cf3a;letter-spacing:1px;text-shadow:2px 3px 4px rgba(0,0,0,.35)}
.hero h1 span{color:#c8161d}
.hero .art{left:385px;top:215px;width:505px;height:235px;border-radius:30px;background:linear-gradient(135deg,#4a4a4a,#1d1d1d 60%,#7b5a3a)}
.hero .splash{left:800px;top:0;width:400px;height:340px;border-radius:0 0 0 60%;background:linear-gradient(200deg,#d8202a 10%,#f3d31a 40%,#8cc63f 60%,#1e74c8 85%,rgba(30,116,200,0) 100%)}

/* section heads */
.sec-title{left:0;width:1200px;text-align:center;font-family:'Bitter',serif;font-weight:700;font-size:28px;color:var(--navy);letter-spacing:.5px}
.sec-title span{color:var(--orange)}
.sec-rule{left:443px;width:314px;height:1px;background:#c9c9c9}
.sec-dot{left:594px;width:12px;height:12px;background:var(--navy);border-radius:50%}

/* services */
.services{left:0;top:607px;width:1200px;height:463px;background:var(--light)}
.card{top:735px;width:216px;height:293px;background:#fff;box-shadow:0 1px 4px rgba(0,0,0,.18);text-align:center}
.card .photo{position:absolute;left:4px;top:4px;width:208px;height:142px}
.card h3{position:absolute;left:0;right:0;top:163px;font-family:'Bitter',serif;font-weight:400;font-size:22px}
.card p{position:absolute;left:14px;right:14px;top:198px;font-size:13px;line-height:18px;color:var(--muted)}
.card .bar{position:absolute;left:0;right:0;bottom:0;height:4px}
.card .plus{position:absolute;left:86px;bottom:0;width:44px;height:22px;border-radius:22px 22px 0 0;color:#fff;font-size:24px;font-weight:700;line-height:26px}

/* about */
.about-band{left:0;top:1070px;width:1200px;height:450px;background:var(--grey)}
.about-heading{left:132px;top:1186px;width:450px;font-size:20px;line-height:28px;color:var(--navy);font-weight:700}
.about-text{left:132px;top:1251px;width:440px;font-size:13px;line-height:25px;color:#333}
.btn{left:132px;top:1438px;width:103px;height:31px;background:var(--navy);color:#fff;border-radius:3px;font-size:13px;text-align:center;line-height:31px}
.device{left:627px;top:1194px;width:441px;height:274px;border-radius:16px;background:#111;box-shadow:0 10px 16px rgba(0,0,0,.3)}
.device .screen{position:absolute;left:33px;top:30px;width:375px;height:213px;background:linear-gradient(135deg,#dfe4ea,#6d7c8c 45%,#1f2833)}

/* why */
.why-item{top:1656px;width:262px;text-align:center}
.why-item .badge{margin:0 auto;width:142px;height:142px;border-radius:50%;border:6px solid #fff;box-shadow:0 0 0 2px rgba(0,0,0,.06);display:flex;align-items:center;justify-content:center;position:relative}
.why-item .badge::after{content:"";position:absolute;inset:6px;border-radius:50%;border:1px dashed rgba(255,255,255,.55)}
.why-item h4{margin-top:31px;font-family:'Bitter',serif;font-weight:400;font-size:23px;line-height:30px;color:#222}
.why-item .line{margin:12px auto 0;width:45px;height:4px}

/* footer */
.footer{left:0;top:1931px;width:1200px;height:250px;background:linear-gradient(180deg,#3a3a3a,#1f1f1f)}
.footer h5{position:absolute;top:29px;font-size:17px;font-weight:700;color:#fff}
.f-rule{position:absolute;top:57px;height:1px;border-top:1px dashed #555}
.f-links{position:absolute;left:132px;top:66px;list-style:none}
.f-links li{font-size:13px;line-height:24px;color:#ddd}
.f-links li::before{content:"›";margin:0 8px 0 4px;color:#bbb}
.f-news{position:absolute;left:320px;top:68px;width:218px;font-size:13px;line-height:19px;color:#ddd}
.f-input{position:absolute;left:320px;top:135px;width:212px;height:29px;background:#fff;border-radius:3px;font-size:12px;font-style:italic;color:#555;padding:7px 9px}
.f-sub{position:absolute;left:320px;top:177px;width:92px;height:27px;background:var(--sky);color:#fff;font-size:12px;font-weight:700;text-align:center;line-height:27px;border-radius:2px}
.f-contact{position:absolute;left:613px;font-size:13px;line-height:18px;color:#ddd;display:flex;gap:14px}
.f-contact svg{flex:none;margin-top:2px}
.map{left:830px;top:2003px;width:238px;height:138px;border:3px solid #fff;background:linear-gradient(135deg,#ece8dd,#ddd8c9 60%,#f1d77a)}
.vdiv{position:absolute;top:35px;width:1px;height:180px;background:#444}
.bottombar{left:0;top:2181px;width:1200px;height:38px;background:var(--navy);color:#fff;font-size:12px}
</style>
</head>
<body>

<div class="abs topbar">
  <div class="abs phone"><i><svg width="14" height="14" viewBox="0 0 24 24"><path fill="#fff" d="M6.6 10.8c1.4 2.8 3.8 5.1 6.6 6.6l2.2-2.2c.3-.3.7-.4 1-.2 1.1.4 2.3.6 3.6.6.6 0 1 .4 1 1V20c0 .6-.4 1-1 1C10.6 21 3 13.4 3 4c0-.6.4-1 1-1h3.5c.6 0 1 .4 1 1 0 1.3.2 2.5.6 3.6.1.3 0 .7-.2 1z"/></svg></i>555-014-2290</div>
  <div class="abs social" style="left:932px;background:#c6b51c"></div>
  <div class="abs social" style="left:968px;background:#2fa3dc"></div>
  <div class="abs social" style="left:1005px;background:#f07f3c"></div>
  <div class="abs social" style="left:1041px;background:#9cc23a"></div>
</div>

<header class="abs header">
  <div class="abs brand"><i></i>Brindle Peak Servers</div>
  <nav class="nav">
    <a class="active" style="left:537px">HOME</a><span class="sep" style="left:601px"></span>
    <a style="left:620px">ABOUT US</a><span class="sep" style="left:714px"></span>
    <a style="left:732px">PRODUCTS</a><span class="sep" style="left:833px"></span>
    <a style="left:851px">PORTFOLIO</a><span class="sep" style="left:956px"></span>
    <a style="left:974px">CONTACT US</a>
  </nav>
</header>

<section class="abs hero">
  <div class="abs splash" role="img" aria-label="Colourful paint splashes"></div>
  <div class="abs art" role="img" aria-label="Tablet with design tools, brushes, globe and palette"></div>
  <h1>GREAT <span>WEB</span> DESIGNING</h1>
</section>

<section class="abs services"></section>
<div class="abs sec-title" style="top:636px">OUR <span>SERVICES</span></div>
<div class="abs sec-rule" style="top:685px"></div>
<div class="abs sec-dot" style="top:679px"></div>

<div class="abs card" style="left:132px">
  <div class="photo" role="img" aria-label="Server room aisle" style="background:linear-gradient(180deg,#2b2b2b,#6a6a6a 50%,#1a1a1a)"></div>
  <h3 style="color:var(--olive)">Web Hosting</h3>
  <p>Lorem ipsum dolor sit amet, consectetuer adipisc inelit, sed diam nonummy nibh.</p>
  <div class="bar" style="background:var(--olive)"></div><div class="plus" style="background:var(--olive)">+</div>
</div>
<div class="abs card" style="left:370px">
  <div class="photo" role="img" aria-label="Colourful puzzle pieces spelling web design" style="background:linear-gradient(135deg,#e94b3c,#f5c12e 45%,#4aa3df)"></div>
  <h3 style="color:var(--blue)">Web Design</h3>
  <p>Lorem ipsum dolor sit amet, consectetuer adipisc inelit, sed diam nonummy nibh.</p>
  <div class="bar" style="background:var(--blue)"></div><div class="plus" style="background:var(--blue)">+</div>
</div>
<div class="abs card" style="left:611px">
  <div class="photo" role="img" aria-label="Support staff wearing headsets" style="background:linear-gradient(135deg,#e8eef4,#b9c6d2 60%,#8a6f5a)"></div>
  <h3 style="color:var(--deep-orange)">Techinical Support</h3>
  <p>Lorem ipsum dolor sit amet, consectetuer adipisc inelit, sed diam nonummy nibh.</p>
  <div class="bar" style="background:var(--deep-orange)"></div><div class="plus" style="background:var(--deep-orange)">+</div>
</div>
<div class="abs card" style="left:852px">
  <div class="photo" role="img" aria-label="Business person holding a tablet with digital icons" style="background:linear-gradient(135deg,#1e2e44,#4d7fae 55%,#c8d8e8)"></div>
  <h3 style="color:var(--lime)">Other Services</h3>
  <p>Lorem ipsum dolor sit amet, consectetuer adipisc inelit, sed diam nonummy nibh.</p>
  <div class="bar" style="background:var(--lime)"></div><div class="plus" style="background:var(--lime)">+</div>
</div>

<section class="abs about-band"></section>
<div class="abs sec-title" style="top:1102px">ABOUT <span>US</span></div>
<div class="abs sec-rule" style="top:1151px"></div>
<div class="abs sec-dot" style="top:1145px"></div>
<h2 class="abs about-heading">We Provide Online &nbsp;Web Hosting to Australian Clients.</h2>
<p class="abs about-text">Lorem ipsum dolor sit amet, consectetuer adipiscing elit, sed diam nonu bmmy nibh euismod tincidunt ut laoreet dolore magna aliquam erat vol utpat. Ut wisi enim ad minim veniam, quis nostrud exerci tation ullamco rper suscipit lobortis nisl ut aliquip ex ea commodo consequat. Duis aut em vel eum iriure dolor in hendrerit in Lorem ipsum dolor sit amet, cons ectetuer adipiscing elit, sed diam nonu bmmy nibh euismod tincidunt ut laoreet dolore magna aliquam erat vol utpat.</p>
<div class="abs btn">Read More</div>
<div class="abs device"><div class="screen" role="img" aria-label="Video still of server racks"></div></div>

<div class="abs sec-title" style="top:1554px">WHY <span>CHOOSE US</span></div>
<div class="abs sec-rule" style="top:1603px"></div>
<div class="abs sec-dot" style="top:1597px"></div>

<div class="abs why-item" style="left:75px">
  <div class="badge" style="background:var(--olive)"><svg width="56" height="56" viewBox="0 0 56 56" fill="none" stroke="#fff" stroke-width="4"><path d="M12 30v-6a16 16 0 0 1 32 0v6"/><rect x="8" y="28" width="8" height="12" rx="3" fill="#fff"/><rect x="40" y="28" width="8" height="12" rx="3" fill="#fff"/><path d="M44 40c0 6-6 8-12 8"/></svg></div>
  <h4>Free 24×7<br>Support</h4><div class="line" style="background:var(--olive)"></div>
</div>
<div class="abs why-item" style="left:337px">
  <div class="badge" style="background:var(--blue)"><svg width="60" height="56" viewBox="0 0 60 56"><path fill="#fff" d="M30 4 4 28h8v24h14V38h8v14h14V28h8z"/></svg></div>
  <h4>Great Value<br>Domain Names</h4><div class="line" style="background:var(--blue)"></div>
</div>
<div class="abs why-item" style="left:600px">
  <div class="badge" style="background:var(--deep-orange)"><span style="font-family:'Bitter',serif;font-weight:700;font-size:64px;color:#fff;line-height:1">$</span></div>
  <h4>Start Your Business<br>For $30</h4><div class="line" style="background:var(--deep-orange)"></div>
</div>
<div class="abs why-item" style="left:863px">
  <div class="badge" style="background:var(--lime)"><svg width="56" height="56" viewBox="0 0 56 56"><path fill="#fff" d="M16 6h24v14a12 12 0 0 1-24 0z"/><path fill="none" stroke="#fff" stroke-width="4" d="M16 11H7v4a9 9 0 0 0 9 9M40 11h9v4a9 9 0 0 1-9 9"/><rect x="25" y="31" width="6" height="11" fill="#fff"/><rect x="17" y="42" width="22" height="7" fill="#fff"/></svg></div>
  <h4>The Best<br>Online Hosting</h4><div class="line" style="background:var(--lime)"></div>
</div>

<footer class="abs footer">
  <h5 style="left:132px">Quick Links</h5><div class="f-rule" style="left:132px;width:115px"></div>
  <ul class="f-links"><li>Home</li><li>About Us</li><li>Products</li><li>Portfolio</li><li>Contact Us</li></ul>
  <div class="vdiv" style="left:280px"></div>
  <h5 style="left:320px">Newsletter Signup</h5><div class="f-rule" style="left:320px;width:218px"></div>
  <p class="f-news">Lorem ipsum dolor sit amet,consecte adipiscing elit, sed diam nonummy ni euismod tincidunt.</p>
  <div class="f-input">Email Address</div>
  <div class="f-sub">SUBSCRIBE</div>
  <div class="vdiv" style="left:573px"></div>
  <h5 style="left:613px">Contact Detail</h5><div class="f-rule" style="left:613px;width:455px"></div>
  <div class="f-contact" style="top:70px;width:200px"><svg width="14" height="18" viewBox="0 0 14 18"><path fill="#fff" d="M7 0a7 7 0 0 0-7 7c0 5 7 11 7 11s7-6 7-11a7 7 0 0 0-7-7zm0 10a3 3 0 1 1 0-6 3 3 0 0 1 0 6z"/></svg><span>Lorem ipsum dolor sit consectetuer adipisc inelit, sed diam nonu</span></div>
  <div class="f-contact" style="top:142px"><svg width="14" height="14" viewBox="0 0 24 24"><path fill="#fff" d="M6.6 10.8c1.4 2.8 3.8 5.1 6.6 6.6l2.2-2.2c.3-.3.7-.4 1-.2 1.1.4 2.3.6 3.6.6.6 0 1 .4 1 1V20c0 .6-.4 1-1 1C10.6 21 3 13.4 3 4c0-.6.4-1 1-1h3.5c.6 0 1 .4 1 1 0 1.3.2 2.5.6 3.6.1.3 0 .7-.2 1z"/></svg><span>(010) 555 0187</span></div>
  <div class="f-contact" style="top:174px"><svg width="14" height="14" viewBox="0 0 14 14"><rect x="3" y="0" width="8" height="4" fill="#fff"/><rect x="0" y="5" width="14" height="6" rx="1" fill="#fff"/><rect x="3" y="9" width="8" height="5" fill="#fff"/></svg><span>(012) 555 0143</span></div>
  <div class="f-contact" style="top:206px"><svg width="14" height="12" viewBox="0 0 14 12"><rect width="14" height="10" y="1" fill="#fff"/><path d="M0 1l7 5 7-5" stroke="#333" fill="none"/></svg><span>info@brindlepeak.example</span></div>
</footer>
<div class="abs map" role="img" aria-label="Street map with office location pin"></div>

<div class="abs bottombar">
  <span class="abs" style="left:132px;top:12px">Copyright © 2015 brindlepeak.example</span>
  <span class="abs" style="left:853px;top:12px">Privacy Policy &nbsp;&nbsp;| &nbsp;&nbsp;Terms &amp; Conditions</span>
</div>

</body>
</html>
```